Stationary Design needed for Physical Therapy and Wellness Center

Letterhead, Envelopes, Business Cards (x2) needed. We are a studio specializing in helping our clients improve mobility, fitness, and recover from injury. We use the Spirolane method and need to adhere to their trademark restrictions.

Target Market(s)

Potential Clients: active people...many from dance or athletic backgrounds.

Industry/Entity Type

Health And Wellness

Font styles to use
Sans Serif
Other font styles liked:
• Times New Roman for the word Spirolane.

Colors
00a990
33b8a4
86cfc6
0393ce
33a6d7
85cae6

Requirements
Must have
• Attention to Spirolane trademark guidelines (Times New Roman font, Bold type, use of registered trademark symbol). Examples of current stationary can be provided as an example.
• Concept of movement, flow.

```html
<!DOCTYPE html>
<html lang="en">
<head>
<meta charset="utf-8">
<title>Kinetra Letterhead</title>
<link rel="stylesheet" href="https://fonts.googleapis.com/css2?family=Tinos:wght@400;700&family=Montserrat:wght@400;500&display=swap">
<style>
  :root {
    --backdrop: #e9e6e1;
    --paper: #fbfaf4;
    --ink: #2b2b2b;
    --ink-soft: #3a3a3a;
    --rule: #4a4a4a;
    --teal: #00a990;
    --teal-mid: #33b8a4;
    --teal-light: #86cfc6;
    --blue: #0393ce;
    --blue-mid: #33a6d7;
    --blue-light: #85cae6;
    --name: #1fa9c6;
  }
  * { box-sizing: border-box; margin: 0; padding: 0; }
  html, body {
    width: 1200px; height: 900px; overflow: hidden;
    background: var(--backdrop);
  }
  .letterhead {
    position: absolute;
    left: 276px; top: 30px;
    width: 649px; height: 840px;
    background: var(--paper);
    box-shadow: 0 2px 10px rgba(0,0,0,0.12);
    overflow: hidden;
  }
  .brand {
    position: absolute; left: 108px; top: 52px;
    display: flex; align-items: center; gap: 10px;
  }
  .brand-dot {
    width: 30px; height: 30px; border-radius: 50%;
    background: var(--teal);
  }
  .brand-name {
    font-family: "Tinos", "Times New Roman", serif;
    font-weight: 700; font-size: 40px; letter-spacing: 0.5px;
    color: var(--ink-soft);
  }
  .divider {
    position: absolute; left: 347px; top: 31px;
    width: 2px; height: 104px; background: var(--rule);
  }
  .practitioner {
    position: absolute; left: 364px; top: 34px;
    font-family: "Tinos", "Times New Roman", serif; font-weight: 700;
  }
  .practitioner-name, .practitioner-degrees {
    color: var(--name); font-size: 18px; line-height: 21px;
  }
  .credentials {
    list-style: none; margin-top: 4px;
    color: var(--ink); font-size: 11px; line-height: 13px;
  }
  .contact {
    position: absolute; right: 16px; top: 780px;
    text-align: right;
    font-family: "Tinos", "Times New Roman", serif; font-weight: 700;
    font-size: 15px; line-height: 19px; color: var(--ink);
  }
  .flow-band {
    position: absolute; left: 0; bottom: 0;
    width: 649px; height: 100px;
  }
</style>
</head>
<body>
  <main class="letterhead">
    <div class="brand">
      <span class="brand-dot"></span>
      <span class="brand-name">Kinetra</span>
    </div>

    <div class="divider"></div>

    <section class="practitioner">
      <p class="practitioner-name">Daniel Moore</p>
      <p class="practitioner-degrees">MSPT, ATC</p>
      <ul class="credentials">
        <li>Licensed Physical Therapist</li>
        <li>Certified Athletic Trainer</li>
        <li>Certified Spirolane<sup>®</sup> instructor</li>
        <li>Figure Skating Coach</li>
      </ul>
    </section>

    <svg class="flow-band" viewBox="0 0 649 100" preserveAspectRatio="none" aria-hidden="true">
      <defs>
        <linearGradient id="flowOuter" x1="0" y1="0" x2="1" y2="0">
          <stop offset="0" stop-color="#1aa6bf"/>
          <stop offset="0.6" stop-color="#1eaa9a"/>
          <stop offset="1" stop-color="#3dbb9f"/>
        </linearGradient>
        <linearGradient id="flowInner" x1="0" y1="0" x2="1" y2="0">
          <stop offset="0" stop-color="#85cae6"/>
          <stop offset="1" stop-color="#5fbfd8"/>
        </linearGradient>
      </defs>
      <path d="M0 18 C120 -4 300 0 450 100 L0 100 Z" fill="url(#flowOuter)"/>
      <path d="M0 40 C90 30 170 50 230 100 L0 100 Z" fill="url(#flowInner)"/>
    </svg>

    <address class="contact" style="font-style: normal;">
      <p>555-310-4827</p>
      <p>daniel@kinetrapt.com</p>
      <p>www.kinetrapt.com</p>
    </address>
  </main>
</body>
</html>
```